The Linden Clinic. Psychotherapy practice. Looking for a multi-use design.

Hello, we need someone who can give us a design that's usable across business cards, rack cards and headed paper.
We're also looking for a logo that can be used on the cards and on the web site when we change the web site.
The current web site, www.the-linden-clinic-example.co.uk can be used to gather info, but does not need to be used for colour/design choices (e.g. one partner likes the Times font another prefers a sans-serif font. One likes the idea of a brass plaque in the design, the other doesn't).
The main point about the design is that it should convey an image of a professional service - their latest strap line is "Professional • Experienced • Confidential" used in a local ad.
Updates
The ladies have also asked me to add that although the Practice is very close to Corvell Minster, and one of the lines they use on the site is "Just a few steps from the Minster", they don't want it to look like something that's Christian or religious.
Thanks.
Industry/Entity Type
Professional Service
Look and feel
Each slider illustrates characteristics of the customer's brand and the style your logo design should communicate.

```html
<!DOCTYPE html>
<html lang="en">
<head>
<meta charset="utf-8">
<title>The Linden Clinic – Business Cards</title>
<link rel="stylesheet" href="https://fonts.googleapis.com/css2?family=Arimo:wght@400;700&family=Open+Sans:wght@400;600&display=swap">
<style>
  :root {
    --page-bg: #e9e7e3;
    --navy: #2c3a7c;
    --blue: #4a5aa8;
    --blue-light: #7d8cc8;
    --brand-blue: #3b4b9c;
    --ink: #1b1b1f;
    --card-white: #ffffff;
    --faint: #eceef3;
    --label: #2a3a86;
  }
  * { box-sizing: border-box; margin: 0; padding: 0; }
  html, body { width: 1200px; height: 784px; overflow: hidden; }
  body {
    background: var(--page-bg);
    font-family: "Open Sans", Arial, sans-serif;
    position: relative;
  }
  .card {
    position: absolute;
    width: 540px;
    height: 310px;
    top: 237px;
    border-radius: 3px;
    overflow: hidden;
    box-shadow: 0 4px 14px rgba(0,0,0,.18);
  }
  /* Back of card */
  .card--back { left: 40px; background: var(--navy); }
  .card--back .pattern {
    position: absolute; inset: 0;
    background: radial-gradient(ellipse at 85% 20%, #8e9bd3 0%, #6675b9 35%, #3f4e96 70%, #2c3a7c 100%);
  }
  .card--back .brand-mark {
    position: absolute; left: 40px; top: 58px;
    width: 104px; height: 104px; border-radius: 50%;
    background: #1f2a63; border: 3px solid #b8bfd9;
  }
  .card--back .brand-name {
    position: absolute; left: 156px; top: 62px;
    font-family: "Arimo", Arial, sans-serif; font-weight: 700;
    font-size: 30px; color: #ffffff; letter-spacing: .2px;
  }
  .card--back .brand-rule {
    position: absolute; left: 150px; top: 102px; width: 350px; height: 2px; background: #ffffff;
  }
  .card--back .brand-sub {
    position: absolute; left: 156px; top: 110px;
    font-family: "Arimo", Arial, sans-serif; font-size: 14px;
    letter-spacing: 5.2px; color: #ffffff;
  }
  .strapline {
    position: absolute; left: 40px; right: 40px; bottom: 40px;
    display: flex; justify-content: space-between;
    list-style: none; color: #ffffff; font-size: 19px;
  }
  .strapline li::before { content: "• "; }

  /* Front of card */
  .card--front { left: 620px; background: var(--card-white); }
  .card--front .faint-disc {
    position: absolute; right: -40px; top: 70px;
    width: 230px; height: 230px; border-radius: 50%;
    background: radial-gradient(circle, #ffffff 0%, var(--faint) 70%, #e3e5eb 100%);
  }
  .card--front .brand-mark {
    position: absolute; left: 30px; top: 40px;
    width: 100px; height: 100px; border-radius: 50%;
    background: #2a3778; border: 2px solid #c9cbd6;
  }
  .card--front .brand-name {
    position: absolute; left: 146px; top: 38px;
    font-family: "Arimo", Arial, sans-serif; font-weight: 700;
    font-size: 31px; color: var(--brand-blue);
  }
  .card--front .brand-rule {
    position: absolute; left: 140px; top: 80px; width: 370px; height: 2px; background: var(--ink);
  }
  .card--front .brand-sub {
    position: absolute; left: 146px; top: 88px;
    font-family: "Arimo", Arial, sans-serif; font-size: 14.5px;
    letter-spacing: 5.4px; color: var(--ink);
  }
  .contacts {
    position: absolute; left: 36px; top: 160px;
    display: grid; grid-template-columns: 60px auto; row-gap: 2px;
    font-size: 14.5px; color: var(--ink); line-height: 19px;
  }
  .contacts .who { color: var(--label); font-weight: 600; font-size: 16px; }
  .contacts .line { display: flex; align-items: center; gap: 6px; }
  .contacts .icon { width: 14px; height: 14px; flex: none; fill: var(--label); }
</style>
</head>
<body>

<section class="card card--back" aria-label="Card back">
  <div class="pattern" role="img" aria-label="Soft blue pattern of overlapping ellipses"></div>
  <div class="brand-mark"></div>
  <div class="brand-name">The Linden Clinic</div>
  <div class="brand-rule"></div>
  <div class="brand-sub">PSYCHOTHERAPY PRACTICE</div>
  <ul class="strapline">
    <li>Professional</li>
    <li>Experienced</li>
    <li>Confidential</li>
  </ul>
</section>

<section class="card card--front" aria-label="Card front">
  <div class="faint-disc"></div>
  <div class="brand-mark"></div>
  <div class="brand-name">The Linden Clinic</div>
  <div class="brand-rule"></div>
  <div class="brand-sub">PSYCHOTHERAPY PRACTICE</div>

  <svg width="0" height="0" style="position:absolute">
    <defs>
      <symbol id="i-phone" viewBox="0 0 16 16"><path d="M3.5 1.5l2.5 0 1 3.5-1.6 1.2a8 8 0 0 0 4.4 4.4L11 9l3.5 1v2.5c0 1-1 2-2 2A11 11 0 0 1 1.5 3.5c0-1 1-2 2-2z"/></symbol>
      <symbol id="i-mail" viewBox="0 0 16 16"><path d="M1 3h14v10H1z M2 4.2v.4l6 4.2 6-4.2v-.4z" fill-rule="evenodd"/></symbol>
      <symbol id="i-web" viewBox="0 0 16 16"><path d="M8 1a7 7 0 1 0 0 14A7 7 0 0 0 8 1zm0 1.5c.8 0 1.7 1.6 2 4H6c.3-2.4 1.2-4 2-4zM2.6 6.5h2c-.1.5-.1 1-.1 1.5s0 1 .1 1.5h-2a5.6 5.6 0 0 1 0-3zm3.4 3h4c-.3 2.4-1.2 4-2 4s-1.7-1.6-2-4zm5.4 0c.1-.5.1-1 .1-1.5s0-1-.1-1.5h2a5.6 5.6 0 0 1 0 3z"/></symbol>
      <symbol id="i-home" viewBox="0 0 16 16"><path d="M8 1.5L1 8h2v6.5h4v-4h2v4h4V8h2z"/></symbol>
    </defs>
  </svg>

  <div class="contacts">
    <span class="who">Maren:</span>
    <span class="line"><svg class="icon"><use href="#i-phone"/></svg>01632 960418 or 07700 900352</span>
    <span></span>
    <span class="line"><svg class="icon"><use href="#i-mail"/></svg>info@lindentherapy-example.co.uk</span>
    <span class="who">Ruth:</span>
    <span class="line"><svg class="icon"><use href="#i-phone"/></svg>07700 900 781</span>
    <span></span>
    <span class="line"><svg class="icon"><use href="#i-mail"/></svg>info@ruthcallard-example.co.uk</span>
    <span></span>
    <span class="line"><svg class="icon"><use href="#i-web"/></svg>www.the-linden-clinic-example.co.uk</span>
    <span></span>
    <span class="line"><svg class="icon"><use href="#i-home"/></svg>12 Vellum Lane, Corvell, CV1 4QX</span>
  </div>
</section>

</body>
</html>
```